Healthcare and Professional IT Services Company need a redesigned business card

We are a IT Services company that targets small medical practices and professional business such as Attorneys, Accounts, Architects etc. We want to communicate a professional yet friendly image using recent logo redesign here on Drafthive. Like to see the colors blue and orange in the design. Must use the Tall Cedar Technology as displayed in the new logo - then also want to incorporate the fish logo as well.

Target Market(s)

Small medical and professional services

Industry/Entity Type

It Company

Contact Information for Business Card

The usual stuff, place for name address phone website. Also maybe our tagline which is "Rooted in technology"

Requirements
Must have
• My new logo and the fish somewhere on the card

```html
<!DOCTYPE html>
<html lang="en">
<head>
<meta charset="UTF-8">
<title>Tall Cedar Technology — Business Card</title>
<link href="https://fonts.googleapis.com/css2?family=Open+Sans:wght@300;400;600&display=swap" rel="stylesheet">
<style>
  :root {
    --canvas: #e6e4e2;
    --card: #ffffff;
    --brand-blue: #1e9ad6;
    --brand-orange: #f39a2b;
    --ink: #4a4a4a;
    --muted: #8a8a8a;
    --fish-light: #e3f3fb;
    --fish-mid: #b9e0f3;
  }
  * { box-sizing: border-box; margin: 0; padding: 0; }
  html, body {
    width: 1200px; height: 997px; overflow: hidden;
    background: var(--canvas);
    font-family: "Open Sans", Arial, sans-serif;
  }
  .sheet {
    width: 1200px; height: 997px;
    display: flex; flex-direction: column; align-items: center; justify-content: center;
    gap: 44px;
  }
  .card {
    width: 800px; height: 457px;
    background: var(--card);
    box-shadow: 0 6px 18px rgba(0,0,0,0.12);
    position: relative; overflow: hidden;
  }

  /* Front */
  .card--front { display: flex; flex-direction: column; align-items: center; justify-content: center; }
  .mascot-small {
    width: 180px; height: 110px; border-radius: 55px;
    background: radial-gradient(ellipse at center, var(--fish-mid), var(--fish-light));
  }
  .wordmark {
    color: var(--brand-blue); font-weight: 600; letter-spacing: 0.3px; white-space: nowrap;
  }
  .card--front .wordmark { font-size: 30px; margin-top: 18px; }
  .tagline {
    color: var(--muted); font-weight: 300; font-size: 20px; letter-spacing: 1.5px;
    margin-top: 34px;
  }

  /* Back */
  .mascot-large {
    position: absolute; left: 0; top: 120px;
    width: 450px; height: 337px;
    border-top-right-radius: 170px;
    background: radial-gradient(ellipse at 45% 40%, var(--fish-mid), var(--fish-light) 70%, var(--card));
  }
  .contact {
    position: absolute; right: 40px; top: 32px;
    text-align: right;
  }
  .contact__name { color: var(--brand-blue); font-size: 26px; font-weight: 400; line-height: 1.2; }
  .contact__role { color: var(--brand-orange); font-size: 17px; margin-top: 2px; }
  .contact__lines { margin-top: 20px; color: var(--ink); font-size: 15px; line-height: 1.6; }
  .contact__row { display: flex; justify-content: flex-end; align-items: center; gap: 10px; white-space: nowrap; }
  .contact__row svg { width: 15px; height: 15px; flex: none; }
  .contact__row--plain { padding-right: 25px; }
  .card--back .wordmark {
    position: absolute; right: 40px; top: 318px;
    font-size: 28px;
  }
</style>
</head>
<body>
<main class="sheet">
  <section class="card card--front">
    <div class="mascot-small" role="img" aria-label="Cartoon fish mascot illustration"></div>
    <div class="wordmark">Tall Cedar Technology</div>
    <p class="tagline">Rooted in technology</p>
  </section>

  <section class="card card--back">
    <div class="mascot-large" role="img" aria-label="Large cartoon fish mascot illustration"></div>
    <div class="contact">
      <h1 class="contact__name">Dana Whitlow</h1>
      <p class="contact__role">CEO/Founder</p>
      <div class="contact__lines">
        <div class="contact__row contact__row--plain">412 Harbor Row</div>
        <div class="contact__row contact__row--plain">Kelp Bay, Alaska 99561</div>
        <div class="contact__row">555 014 2290
          <svg viewBox="0 0 16 16" aria-hidden="true"><path fill="#1e9ad6" d="M3.5 1.5l2.2 2.6-1.3 1.6c.8 1.9 2.1 3.2 4 4l1.6-1.3 2.6 2.2-1.4 2.1C6.4 12.4 3.6 9.6 1.3 4.8z"/></svg>
        </div>
        <div class="contact__row">hello@tallcedar.example
          <svg viewBox="0 0 16 16" aria-hidden="true"><rect x="1.5" y="3.5" width="13" height="9" rx="1" fill="none" stroke="#1e9ad6" stroke-width="1.6"/><path d="M2 4l6 5 6-5" fill="none" stroke="#1e9ad6" stroke-width="1.6"/></svg>
        </div>
        <div class="contact__row">www.tallcedar.example
          <svg viewBox="0 0 16 16" aria-hidden="true"><circle cx="8" cy="8" r="6.5" fill="#1e9ad6"/><path d="M1.5 8h13M8 1.5c-2.5 3-2.5 10 0 13M8 1.5c2.5 3 2.5 10 0 13" fill="none" stroke="#fff" stroke-width="1"/></svg>
        </div>
      </div>
    </div>
    <div class="wordmark">Tall Cedar Technology</div>
  </section>
</main>
</body>
</html>
```